Design Concept for various leaflets and banners etc

Create a print design concept that can be utilized across multiple formats eg leaflets, booklets, banners, website.We currently have an collection of print materials with various design styles. We wish to create a look which makes these items more cohesive as a group.The creative should sit comfortably with existing A5 landscape brochure artwork and exhibition banners. The design concept provided should have no inherent meaning in itself. Preferred colours are blue and green. The colours used should be in-keeping with the colour guide attached. This look will mainly be employed on A6 flyers, DL Flyers, business cards and signage.The look should be simple yet modern and serious. The look should allow maximum flexibility in deployment. (Epically considering we have over 30 different leaflets that need to be visibly different but yet seen as a family of leaflets.) Our main website address is also our ‘brand’ ie www.Vel-oran.net . We also have a sister project called the Marrow Exhibition.

Target Market(s)

Public

Industry/Entity Type

Christian

Requirements
Must have
• Flexibility in application.
Should not have
• No inherent meaning

```html
<!DOCTYPE html>
<html lang="en">
<head>
<meta charset="utf-8">
<title>Billboard – Christ Jesus came into the world to save sinners</title>
<link href="https://fonts.googleapis.com/css2?family=Raleway:wght@600;700;800&display=swap" rel="stylesheet">
<style>
  :root {
    --navy: #1b2b52;
    --ink: #14223f;
    --teal: #1f9aa6;
    --green: #2fbf9a;
    --orange: #f0653a;
    --gold: #f6bf2b;
    --paper: #ffffff;
    --backdrop: #e9edf2;
  }
  html, body {
    margin: 0;
    width: 1200px;
    height: 1200px;
    overflow: hidden;
    background: var(--backdrop);
    font-family: "Raleway", sans-serif;
  }
  .board {
    position: absolute;
    left: 40px;
    top: 319px;
    width: 1120px;
    height: 562px;
    background: var(--paper);
    overflow: hidden;
    box-shadow: 0 6px 24px rgba(20, 34, 63, 0.18);
  }
  .board-swoosh {
    position: absolute;
    inset: 0;
    width: 100%;
    height: 100%;
  }
  .headline {
    position: absolute;
    left: 0;
    right: 0;
    top: 128px;
    margin: 0;
    text-align: center;
    color: var(--ink);
    font-weight: 800;
    font-size: 64px;
    line-height: 76px;
    letter-spacing: 0.5px;
  }
  .reference {
    position: absolute;
    right: 135px;
    top: 287px;
    margin: 0;
    color: var(--teal);
    font-weight: 700;
    font-size: 22px;
  }
  .divider {
    position: absolute;
    left: 103px;
    width: 893px;
    top: 336px;
    border-top: 4px dotted var(--teal);
  }
  .call-to-action {
    position: absolute;
    left: 0;
    right: 0;
    top: 356px;
    margin: 0;
    text-align: center;
    color: var(--orange);
    font-weight: 800;
    font-size: 54px;
  }
  .contact {
    position: absolute;
    display: flex;
    align-items: center;
    color: var(--ink);
    font-weight: 700;
  }
  .contact-mail { left: 92px; top: 446px; gap: 28px; }
  .contact-mail address {
    font-style: normal;
    font-size: 24px;
    line-height: 31px;
  }
  .contact-phone { left: 591px; top: 458px; gap: 28px; }
  .contact-phone span { font-size: 38px; letter-spacing: 0.5px; }
</style>
</head>
<body>
  <main class="board">
    <svg class="board-swoosh" viewBox="0 0 1120 562" aria-hidden="true">
      <defs>
        <linearGradient id="swooshGradient" x1="0" y1="1" x2="1" y2="0">
          <stop offset="0" stop-color="#1f8fb0"/>
          <stop offset="1" stop-color="#2fbf9a"/>
        </linearGradient>
      </defs>
      <path d="M0 0 H150 Q45 22 0 82 Z" fill="var(--navy)"/>
      <path d="M0 188 Q45 48 155 0 H138 Q32 42 0 150 Z" fill="var(--teal)"/>
      <path d="M1120 273 Q1070 480 872 562 H900 Q1090 500 1120 328 Z" fill="url(#swooshGradient)"/>
      <path d="M1120 385 Q1070 505 890 562 H1120 Z" fill="var(--navy)"/>
    </svg>

    <h1 class="headline">CHRIST JESUS CAME INTO<br>THE WORLD TO SAVE SINNERS</h1>
    <p class="reference">1 TIMOTHY 1 VERSE 15</p>
    <div class="divider"></div>
    <p class="call-to-action">Read your Bible!</p>

    <div class="contact contact-mail">
      <svg width="44" height="40" viewBox="0 0 44 40" aria-hidden="true">
        <path d="M2 16 L22 2 L42 16 V38 H2 Z" fill="var(--gold)"/>
        <rect x="9" y="6" width="26" height="20" fill="#fff" stroke="var(--gold)" stroke-width="2"/>
        <path d="M13 11 H31 M13 16 H31 M13 21 H25" stroke="var(--gold)" stroke-width="2"/>
        <path d="M2 18 L22 30 L42 18 V38 H2 Z" fill="var(--gold)"/>
        <path d="M2 38 L18 27 M42 38 L26 27" stroke="#fff" stroke-width="2"/>
      </svg>
      <address>P.O. BOX 48<br>ELLANDRA QLD 4599</address>
    </div>

    <div class="contact contact-phone">
      <svg width="36" height="36" viewBox="0 0 36 36" aria-hidden="true">
        <path d="M8 3 L14 10 L10 15 Q14 23 21 26 L26 22 L33 28 L28 34 Q12 32 3 10 Z" fill="var(--gold)"/>
        <path d="M21 4 A11 11 0 0 1 32 15 M20 10 A6 6 0 0 1 26 16" fill="none" stroke="var(--gold)" stroke-width="2.5" stroke-linecap="round"/>
      </svg>
      <span>0400 318 207</span>
    </div>
  </main>
</body>
</html>
```